Veloma Realty Business Cards template for all our agents.

Create a template for Business Cards for our agents. We would need to have access to the source file in order to change info for each agent. We want color and not all white cards. We would like to see movements and texture in the design. Use the colors in the file included plus neutral colors back, white and grey. we would like to see some designs with the logo on the front and some on the back.

Target Market(s)

Real Estate

Industry/Entity Type

Real Estate

Contact Information for Business Card

Please create a template for our business cards. Dimensions 3.5 x 2

We would like
• Spot for an agent photo. (On front of card)
• Logo
• Position (mainly Homeguild ®)
• Mobile
• Fax.
• Email
• Website
• Equal housing logo
• Homeguild logo
• Text – “Search property listings like an agent!”
• Our address 4527 Fennick Row, Suite 3, Clarksburg, MD 20874
• Our colors are attached.
• Not boxy
• DO NOT HAVE AGENT PHOTO CUT OUT.

Requirements
Must have
• • Spot for an agent photo. (On front of card)
• • Logo
• • Position (mainly Homeguild ®)
• • Mobile
• • Fax.
• • Email
• • Website
• • Equal housing logo
• • Homeguild logo
• • Text – “Search property listings like an agent!”
• • Our address 4527 Fennick Row, Suite 3, Clarksburg, MD 20874
Should not have
• BOXY

```html
<!DOCTYPE html>
<html lang="en">
<head>
<meta charset="utf-8">
<title>Veloma Realty Group – Agent Business Card</title>
<link href="https://fonts.googleapis.com/css2?family=Roboto:wght@400;500;700&display=swap" rel="stylesheet">
<style>
  :root {
    --green: #5e7338;
    --green-dark: #3e5424;
    --green-brand: #4f6a2f;
    --maroon: #4e2238;
    --grey-light: #d6d6d6;
    --grey-mid: #a8a8a8;
    --ink: #2a2a2a;
    --white: #ffffff;
    --backdrop: #ecebe8;
  }
  html, body {
    margin: 0;
    width: 1200px;
    height: 1000px;
    overflow: hidden;
    background: var(--backdrop);
  }
  .canvas { display: block; width: 1200px; height: 1000px; }
  .sans { font-family: "Roboto", Arial, sans-serif; }
  .brand-main { font-weight: 500; letter-spacing: 2px; }
  .tagline { font-size: 15px; fill: var(--white); }
  .agent-name { font-size: 24px; font-weight: 700; fill: var(--white); }
  .agent-role { font-size: 13px; font-weight: 500; fill: var(--white); }
  .contact { font-size: 14px; fill: var(--ink); }
  .contact-strong { font-weight: 700; fill: var(--maroon); }
  .icon { fill: var(--maroon); }
</style>
</head>
<body>
<svg class="canvas sans" viewBox="0 0 1200 1000" xmlns="http://www.w3.org/2000/svg">
  <defs>
    <linearGradient id="card-grey" x1="0" y1="0" x2="1" y2="1">
      <stop offset="0" stop-color="var(--grey-mid)"/>
      <stop offset="0.5" stop-color="var(--grey-light)"/>
      <stop offset="1" stop-color="var(--grey-mid)"/>
    </linearGradient>
    <linearGradient id="photo-tone" x1="0" y1="0" x2="1" y2="1">
      <stop offset="0" stop-color="#e9eef2"/>
      <stop offset="0.5" stop-color="#b89c86"/>
      <stop offset="1" stop-color="#8fa3b8"/>
    </linearGradient>
    <clipPath id="back-shape">
      <path d="M273 525 H936 V840 Q936 946 830 946 H273 Z"/>
    </clipPath>
  </defs>

  <!-- Card back: brand side -->
  <g class="card-brand-side">
    <path d="M273 64 H820 Q936 64 936 190 V485 H400 Q273 485 273 340 Z" fill="var(--green)"/>
    <path d="M345 457 H936 V485 H400 Q365 485 345 457 Z" fill="var(--maroon)"/>
    <text class="tagline" x="605" y="472" text-anchor="middle">Search property listings like an agent!</text>
    <rect x="378" y="202" width="120" height="118" fill="var(--white)"/>
    <text class="brand-main" x="512" y="274" font-size="72" fill="var(--white)" textLength="328" lengthAdjust="spacingAndGlyphs">VELOMA</text>
    <text class="brand-main" x="515" y="312" font-size="34" fill="var(--white)" textLength="323" lengthAdjust="spacingAndGlyphs">REALTY GROUP</text>
  </g>

  <!-- Card front: agent side -->
  <g class="card-agent-side" clip-path="url(#back-shape)">
    <rect x="273" y="525" width="663" height="421" fill="url(#card-grey)"/>
    <path class="swoosh-green" d="M540 640 C600 760, 620 860, 615 946 H545 C560 820, 560 720, 540 640 Z" fill="var(--green)"/>
    <path class="swoosh-maroon" d="M498 525 H516 C580 620, 580 820, 562 946 H545 C562 820, 562 620, 498 525 Z" fill="var(--maroon)"/>
    <path class="agent-photo" role="img" aria-label="Agent portrait photo" d="M273 946 V630 Q273 525 378 525 H498 C560 620, 562 820, 545 946 Z" fill="url(#photo-tone)"/>

    <rect x="592" y="557" width="72" height="80" fill="var(--maroon)"/>
    <text class="brand-main" x="680" y="606" font-size="50" fill="var(--green-brand)" textLength="225" lengthAdjust="spacingAndGlyphs">VELOMA</text>
    <text class="brand-main" x="684" y="632" font-size="24" fill="var(--green-brand)" textLength="220" lengthAdjust="spacingAndGlyphs">REALTY GROUP</text>

    <rect class="name-bar" x="558" y="717" width="357" height="54" fill="var(--green-dark)"/>
    <text class="agent-name" x="641" y="745">DANIEL MARSH</text>
    <text class="agent-role" x="641" y="763">REAL ESTATE SALESPERSON</text>

    <text class="contact" x="637" y="810">4527 Fennick Row, Suite 3,</text>
    <text class="contact" x="637" y="828">Clarksburg, MD 20874</text>

    <rect class="badge" x="846" y="797" width="24" height="25" fill="var(--ink)"/>
    <rect class="badge" x="882" y="797" width="24" height="25" fill="var(--ink)"/>

    <path class="icon" d="M637 842 q2-2 4 0 l2 3 q1 1 -1 2 q1 3 4 4 q1-2 2-1 l3 2 q2 2 0 4 q-3 2 -8-2 q-5-5 -6-12 z"/>
    <text class="contact" x="655" y="853">(402) 555-0141</text>
    <rect class="icon" x="637" y="864" width="11" height="8" rx="1"/>
    <rect class="icon" x="639" y="860" width="7" height="3"/>
    <text class="contact" x="655" y="873">(402) 555-0178</text>
    <rect class="icon" x="637" y="883" width="11" height="8" rx="1"/>
    <text class="contact" x="655" y="892">daniel@velomarealtygroup.com</text>
    <circle class="icon" cx="642.5" cy="906" r="5.5"/>
    <text class="contact" x="655" y="911">www.<tspan class="contact-strong">velomarealtygroup</tspan>.com</text>
  </g>
</svg>
</body>
</html>
```